Powerpoint Presentation Template

Kindly design a business class Powepoint Presentation template for our business use. Please stick to our company colours or even pictures as shown on our website and Logo

```html
<!DOCTYPE html>
<html lang="en">
<head>
<meta charset="utf-8">
<title>Marula Ridge Properties – Presentation Template</title>
<link href="https://fonts.googleapis.com/css2?family=Montserrat:wght@300;400;500;600&display=swap" rel="stylesheet">
<style>
:root{
  --wine:#98392d;
  --wine-dark:#7a2c22;
  --wine-soft:rgba(152,57,45,.88);
  --ink:#2b2b2b;
  --muted:#6d6d6d;
  --paper:#ffffff;
  --stage:#8c8c8c;
  --band:#d9d9d9;
}
*{box-sizing:border-box;margin:0;padding:0}
html,body{width:1200px;height:1200px;overflow:hidden;background:var(--stage);font-family:'Montserrat',sans-serif;color:var(--ink)}
.deck{position:absolute;left:8px;top:36px;display:grid;grid-template-columns:repeat(4,290px);grid-auto-rows:162px;column-gap:8px;row-gap:34px}
.slide{position:relative;overflow:hidden;background:var(--paper)}
.abs{position:absolute}
.title{position:absolute;left:0;right:0;top:9px;text-align:center;font-size:11.5px;font-weight:400;letter-spacing:.3px;color:var(--ink)}
.title b{font-weight:400;color:var(--wine)}
.title.sm{font-size:9.5px}
.tiny{font-size:4.4px;line-height:1.45;color:var(--muted)}
.tiny.w{color:#f3dcd8}
.label{font-size:5px;line-height:1.3;color:var(--ink)}
.foot{position:absolute;left:0;right:0;bottom:0;height:3px;background:var(--wine)}
.brand{position:absolute;left:14px;bottom:5px;font-size:5.5px;font-weight:600;color:var(--wine);letter-spacing:.2px}
.num{position:absolute;left:2px;bottom:3px;width:9px;height:9px;background:#333;color:#fff;font-size:4px;line-height:9px;text-align:center}
.url{position:absolute;right:6px;bottom:5px;font-size:3.4px;color:var(--muted)}
.photo{position:absolute}
.ph-gray{background:linear-gradient(180deg,#d8d8d8 0%,#9a9a9a 55%,#5e5e5e 100%)}
.ph-sky{background:linear-gradient(180deg,#8fb3d6 0%,#c9d6df 45%,#b9b2a6 70%,#7f7465 100%)}
.ph-build{background:linear-gradient(180deg,#9cc0e0 0%,#e7e5e0 40%,#c8b8a4 75%,#6f6656 100%)}
.ph-earth{background:linear-gradient(180deg,#a9b9c9 0%,#b58a66 45%,#8f5a3a 100%)}
.ph-road{background:linear-gradient(180deg,#b8c4cc 0%,#8a9179 45%,#55575a 100%)}
.ph-dark{background:linear-gradient(135deg,#5a2a22 0%,#2f2a28 60%,#7b5b45 100%)}
.redbox{position:absolute;background:var(--wine-soft);color:#fff;font-size:5.5px;text-align:center;display:flex;align-items:center;justify-content:center;line-height:1.3;letter-spacing:.2px}
.redbox.cap{font-size:5px;white-space:nowrap}
.circle-ic{fill:var(--wine)}
</style>
</head>
<body>
<main class="deck">

<section class="slide">
  <div class="photo ph-gray" style="inset:0" role="img" aria-label="Black and white photo of a modern residential complex with trees"></div>
  <div class="abs" style="left:60px;right:0;bottom:0;height:55px;background:linear-gradient(90deg,rgba(255,255,255,0),#fff 30%)"></div>
  <div class="abs" style="left:76px;bottom:18px;font-size:8px;font-weight:600;color:var(--wine)">Marula Ridge</div>
  <div class="abs" style="left:150px;top:116px;width:1px;height:30px;background:#444"></div>
  <div class="abs" style="left:158px;top:114px;font-size:11px;line-height:1.25;color:#222">MARULA RIDGE<br>PROPERTIES</div>
  <div class="abs" style="left:158px;top:146px;font-size:6.5px;color:#222">PRESENTATION</div>
</section>

<section class="slide" style="background:var(--wine)">
  <div class="photo" style="inset:0;background:linear-gradient(120deg,#a4473a,#8e372c 60%,#9e4336)" role="img" aria-label="Red tinted photo of a building facade"></div>
  <div class="abs" style="left:36px;top:42px;width:52px;height:52px;border:5px solid #5a1f18;background:#7d2f25"></div>
  <div class="abs" style="left:48px;top:70px;font-size:8.5px;color:#fff;line-height:1.3">WELCOME<br>MESSAGE</div>
  <div class="abs tiny w" style="left:126px;top:62px;width:110px;font-size:4.8px">Lorem ipsum dolor sit amet, elit, sed diam nonummy nibh euismod tincidunt ut laoreet dolore magna aliquam erat volutpat.</div>
  <div class="abs" style="left:0;right:0;bottom:8px;text-align:center;font-size:4px;color:#f3dcd8">www.marularidge.com</div>
</section>

<section class="slide">
  <div class="photo ph-build" style="inset:0" role="img" aria-label="Photo of the company head office entrance with palm trees"></div>
  <svg class="abs" style="left:0;top:0" width="290" height="162"><polygon points="0,0 95,0 150,162 0,162" fill="#98392d"/></svg>
  <div class="abs" style="left:22px;top:8px;font-size:10.5px;color:#fff">ABOUT US</div>
  <div class="abs" style="left:22px;top:42px;width:96px;font-size:5.6px;line-height:1.35;color:#fff">Marula Ridge Properties has delivered over 77 major construction projects worth over R 6.7 Billion in South Africa since inception in March 2001.</div>
  <div class="abs tiny w" style="left:22px;top:104px;width:96px">We have received 8 awards for the quality, professionalism and diligence with which we deliver on construction projects, bearing testimony to our culture of service excellence.</div>
  <div class="brand" style="color:#fff">Marula Ridge</div>
  <div class="num">3</div>
  <div class="url">www.marularidge.com</div>
</section>

<section class="slide">
  <div class="title" style="left:120px">OUR <b>MISSION</b></div>
  <svg class="abs" style="left:0;top:55px" width="110" height="56"><rect x="0" y="10" width="70" height="36" fill="#98392d"/><circle cx="78" cy="28" r="28" fill="#c9c9c9"/><circle cx="70" cy="28" r="26" fill="#98392d"/><path d="M58 26 l8 -6 l8 4 l8 -2 l-4 10 l-8 6 l-8 -4z" fill="#fff"/></svg>
  <div class="abs tiny" style="left:138px;top:54px;width:118px"><span style="color:var(--wine);font-size:5.5px">Our mission</span> is to develop significant partnerships with all our clients, business partners and beneficiaries. Marula Ridge Properties provides top quality services with honesty, integrity and professionalism.<br><br>We aim to participate in the creation of an environment that maximises sustainable growth of all stakeholders, provides affordable and sustainable housing and infrastructure, employment and wealth creation.</div>
  <div class="foot"></div><div class="brand">Marula Ridge</div><div class="num">4</div><div class="url">www.marularidge.com</div>
</section>

<section class="slide">
  <div class="title" style="right:110px">OUR <b>VISION</b></div>
  <svg class="abs" style="left:0;top:42px" width="110" height="64"><rect x="0" y="14" width="70" height="36" fill="#98392d"/><circle cx="82" cy="32" r="30" fill="#c9c9c9"/><circle cx="74" cy="32" r="28" fill="#98392d"/><path d="M64 32 l10 -9 l10 9 v10 h-20z" fill="#fff"/></svg>
  <div class="abs tiny" style="left:114px;top:52px;width:124px"><span style="color:var(--wine);font-size:5.5px">Our vision</span> is to be a vibrant, self-driven organisation achieving distinction in the development of housing and infrastructure solutions.<br><br>As a South African company, we aim to become the preferred supplier for projects related to social development and the economic wellbeing of our society.</div>
  <div class="foot"></div><div class="brand">Marula Ridge</div><div class="num">5</div><div class="url">www.marularidge.com</div>
</section>

<section class="slide">
  <div class="title">OUR <b>SERVICES</b></div>
  <svg class="abs" style="left:0;top:0" width="290" height="162">
    <g class="circle-ic">
      <circle cx="52" cy="48" r="10"/><circle cx="108" cy="48" r="10"/><circle cx="166" cy="48" r="10"/><circle cx="226" cy="48" r="10"/>
      <circle cx="52" cy="100" r="10"/><circle cx="108" cy="100" r="10"/><circle cx="166" cy="100" r="10"/><circle cx="226" cy="100" r="10"/>
    </g>
    <g fill="#fff">
      <path d="M47 53 v-6 l5 -4 l5 4 v6z"/><rect x="104" y="43" width="8" height="10"/><path d="M160 53 v-6 a6 6 0 0 1 12 0 v6z"/><path d="M221 51 l8 -8 l2 2 l-8 8z"/>
      <rect x="47" y="96" width="10" height="7"/><path d="M108 93 q5 7 0 12 q-5 -5 0 -12z"/><path d="M160 104 v-6 l6 -5 l6 5 v6z"/><circle cx="226" cy="100" r="5"/>
    </g>
  </svg>
  <div class="abs label" style="left:32px;top:61px;width:40px;text-align:center">Residential<br>Buildings</div>
  <div class="abs label" style="left:88px;top:61px;width:40px;text-align:center">Commercial<br>Buildings</div>
  <div class="abs label" style="left:146px;top:61px;width:40px;text-align:center">Public<br>Buildings</div>
  <div class="abs label" style="left:206px;top:61px;width:40px;text-align:center">Civil<br>Construction</div>
  <div class="abs label" style="left:32px;top:113px;width:40px;text-align:center">Roads &amp;<br>Earthworks</div>
  <div class="abs label" style="left:88px;top:113px;width:40px;text-align:center">Water &amp;<br>Sanitation</div>
  <div class="abs label" style="left:146px;top:113px;width:40px;text-align:center">Civil<br>Structures</div>
  <div class="abs label" style="left:200px;top:113px;width:52px;text-align:center">Property<br>Development</div>
  <div class="foot"></div><div class="brand">Marula Ridge</div><div class="num">6</div><div class="url">www.marularidge.com</div>
</section>

<section class="slide">
  <div class="title">ACCREDITATION</div>
  <svg class="abs" style="left:0;top:0" width="290" height="162" fill="none" stroke="#333" stroke-width=".6">
    <path d="M32 40 H256 M32 40 V62 M92 40 V62 M150 40 V62 M196 40 V62 M256 40 V62"/>
    <g stroke="#98392d" stroke-width="2" fill="#fff"><circle cx="115" cy="40" r="3.5"/><circle cx="130" cy="40" r="3.5"/><circle cx="145" cy="40" r="3.5"/><circle cx="160" cy="40" r="3.5"/><circle cx="175" cy="40" r="3.5"/></g>
    <g stroke="none" fill="#b7b7b7"><rect x="20" y="64" width="24" height="16"/><rect x="80" y="66" width="26" height="12"/><rect x="136" y="64" width="30" height="16"/><circle cx="186" cy="72" r="7"/><rect x="196" y="68" width="20" height="8"/><circle cx="244" cy="72" r="7"/><rect x="254" y="68" width="20" height="8"/></g>
  </svg>
  <div class="abs tiny" style="left:16px;top:86px;width:44px">Registered with the Builders Quality Board</div>
  <div class="abs tiny" style="left:78px;top:86px;width:46px">Grade 9 general building and civil engineering works</div>
  <div class="abs tiny" style="left:136px;top:86px;width:44px">We are an ISO 9001 certified construction company</div>
  <div class="abs tiny" style="left:182px;top:86px;width:48px">Workplace injury cover with the Safety Fund</div>
  <div class="abs tiny" style="left:238px;top:86px;width:46px">Equity Rating Bureau level 2 rating</div>
  <div class="foot"></div><div class="brand">Marula Ridge</div><div class="num">7</div><div class="url">www.marularidge.com</div>
</section>

<section class="slide">
  <div class="title">AWARDS</div>
  <div class="abs" style="left:0;right:0;top:60px;height:26px;background:var(--band)"></div>
  <svg class="abs" style="left:0;top:0" width="290" height="162">
    <g fill="none" stroke="#98392d" stroke-width="1.4"><circle cx="44" cy="73" r="10"/><circle cx="94" cy="73" r="10"/><circle cx="146" cy="73" r="10"/><circle cx="196" cy="73" r="10"/><circle cx="246" cy="73" r="10"/></g>
    <g fill="#98392d" font-family="Montserrat,sans-serif" font-size="5.5" font-weight="600" text-anchor="middle"><text x="44" y="75">2003</text><text x="94" y="75">2007</text><text x="146" y="75">2008</text><text x="196" y="75">2008</text><text x="246" y="75">2009</text></g>
    <path d="M44 58 V63 M146 58 V63 M246 58 V63 M94 84 V92 M196 84 V92" stroke="#333" stroke-width=".5"/>
  </svg>
  <div class="abs tiny" style="left:16px;top:32px;width:56px;text-align:center">National Housing Developer of the Year Award <span style="color:var(--wine)">National Housing Institute</span></div>
  <div class="abs tiny" style="left:118px;top:32px;width:56px;text-align:center">Contractor of the Year in Difficult Terrain <span style="color:var(--wine)">Provincial Housing Awards</span></div>
  <div class="abs tiny" style="left:218px;top:32px;width:56px;text-align:center">Contractor of the Year in Difficult Terrain <span style="color:var(--wine)">Provincial Housing Awards</span></div>
  <div class="abs tiny" style="left:62px;top:94px;width:66px;text-align:center">Certificate of Appreciation for completing homes in a Difficult Terrain campaign <span style="color:var(--wine)">Department of Housing</span></div>
  <div class="abs tiny" style="left:166px;top:94px;width:60px;text-align:center">Housing Developer of the Year (1400 units) <span style="color:var(--wine)">National Housing Institute</span></div>
  <div class="foot"></div><div class="brand">Marula Ridge</div><div class="num">8</div><div class="url">www.marularidge.com</div>
</section>

<section class="slide">
  <div class="title" style="right:60px">TIMELINE <b>HISTORY</b></div>
  <svg class="abs" style="left:0;top:0" width="290" height="162">
    <path d="M14 120 Q130 118 180 82 T278 12" fill="none" stroke="#333" stroke-width=".8"/>
    <path d="M272 12 l8 -4 l-3 8z" fill="#333"/>
    <g fill="#98392d"><circle cx="26" cy="120" r="3"/><circle cx="46" cy="118" r="3"/><circle cx="82" cy="114" r="3"/><circle cx="114" cy="108" r="3"/><circle cx="144" cy="99" r="3"/><circle cx="174" cy="86" r="3"/><circle cx="204" cy="68" r="3"/><circle cx="224" cy="54" r="3"/><circle cx="246" cy="36" r="3"/><circle cx="264" cy="24" r="3"/></g>
    <g fill="#98392d" font-family="Montserrat,sans-serif" font-size="7" font-weight="600"><text x="14" y="112">1997</text><text x="40" y="130">2001</text><text x="78" y="106">2001</text><text x="100" y="124">2003</text><text x="136" y="92">2004</text><text x="160" y="102">2008</text><text x="192" y="80">2010</text><text x="218" y="82">2015</text><text x="238" y="30">2016</text><text x="260" y="38">2017</text></g>
  </svg>
  <div class="abs tiny" style="left:12px;top:92px;width:34px;font-size:3.4px">Led by the founding member, Kestrel Holdings is launched.</div>
  <div class="abs tiny" style="left:72px;top:82px;width:34px;font-size:3.4px">Opening of regional office.</div>
  <div class="abs tiny" style="left:136px;top:64px;width:36px;font-size:3.4px">First donation by the founder's foundation.</div>
  <div class="abs tiny" style="left:186px;top:44px;width:36px;font-size:3.4px">Foundation donates towards refurbishing schools.</div>
  <div class="abs tiny" style="left:46px;top:134px;width:34px;font-size:3.4px">Inception of Marula Ridge.</div>
  <div class="abs tiny" style="left:106px;top:130px;width:36px;font-size:3.4px">Focus shifts to property development.</div>
  <div class="abs tiny" style="left:166px;top:110px;width:38px;font-size:3.4px">Awarded housing developer of the year.</div>
  <div class="abs tiny" style="left:226px;top:88px;width:36px;font-size:3.4px">New milestone and first billion contract.</div>
  <div class="abs tiny" style="left:258px;top:44px;width:30px;font-size:3.4px">New team appointed to lead growth.</div>
  <div class="foot"></div><div class="brand">Marula Ridge</div><div class="num">9</div><div class="url">www.marularidge.com</div>
</section>

<section class="slide" style="background:var(--wine)">
  <div class="abs" style="left:0;right:0;top:9px;text-align:center;font-size:11.5px;color:#fff">EDITABLE CHART</div>
  <svg class="abs" style="left:48px;top:28px" width="200" height="110" font-family="Montserrat,sans-serif" font-size="4.2" fill="#fff">
    <g stroke="#c27468" stroke-width=".5" fill="none">
      <rect x="0" y="0" width="200" height="110"/>
      <path d="M0 11H200M0 22H200M0 33H200M0 44H200M0 55H200M0 66H200M0 77H200M0 88H200M0 99H200M8 0V110"/>
    </g>
    <text x="2" y="8">1</text><text x="12" y="8">Technology driven business</text>
    <text x="2" y="19">2</text><text x="12" y="19">On time, on budget guarantee</text>
    <text x="2" y="30">3</text><text x="12" y="30">Fixed, all inclusive pricing</text>
    <text x="2" y="41">4</text><text x="12" y="41">360 degree feedback</text>
    <text x="2" y="52">5</text><text x="12" y="52">Preferred suppliers by city and region</text>
    <text x="2" y="63">6</text><text x="12" y="63">Client contact information provided on booking</text>
    <text x="2" y="74">7</text><text x="12" y="74">Reconfirmation 4 hours prior to all bookings</text>
    <text x="2" y="85">8</text><text x="12" y="85">Pre trip site safety declarations</text>
    <text x="2" y="96">9</text><text x="12" y="96">Locally based 24 hour call centre</text>
    <text x="1" y="107">10</text><text x="12" y="107">Booking 24 hours a day with easy to use online portal</text>
  </svg>
  <div class="brand" style="color:#fff">Marula Ridge</div><div class="num">10</div>
</section>

<section class="slide">
  <div class="photo ph-gray" style="inset:0;opacity:.55" role="img" aria-label="Faded photo of modern apartment blocks"></div>
  <div class="abs" style="inset:0;background:rgba(240,240,240,.55)"></div>
  <div class="title" style="top:6px">EDITABLE <b>CHART</b></div>
  <svg class="abs" style="left:0;top:0" width="290" height="162" font-family="Montserrat,sans-serif">
    <g fill="#fff" stroke="#c9c9c9" stroke-width="4"><circle cx="74" cy="72" r="14"/><circle cx="146" cy="72" r="14"/><circle cx="218" cy="72" r="14"/></g>
    <g fill="none" stroke="#98392d" stroke-width="4">
      <circle cx="74" cy="72" r="14" stroke-dasharray="63.3 88" transform="rotate(-90 74 72)"/>
      <circle cx="146" cy="72" r="14" stroke-dasharray="57.2 88" transform="rotate(-90 146 72)"/>
      <circle cx="218" cy="72" r="14" stroke-dasharray="78.3 88" transform="rotate(-90 218 72)"/>
    </g>
    <g font-size="7.5" text-anchor="middle" fill="#333"><text x="74" y="75">72%</text><text x="146" y="75">65%</text><text x="218" y="75">89%</text></g>
    <g font-size="5.5" text-anchor="middle" fill="#98392d"><text x="74" y="100">INFORMATION</text><text x="146" y="100">INFORMATION</text><text x="218" y="100">INFORMATION</text></g>
  </svg>
  <div class="abs tiny" style="left:46px;top:104px;width:56px;color:#333">Lorem ipsum dolor sit amet, elit, sed diam nonummy nibh euismod tincidunt ut laoreet dolore magna aliquam erat volutpat.</div>
  <div class="abs tiny" style="left:118px;top:104px;width:56px;color:#333">Lorem ipsum dolor sit amet, elit, sed diam nonummy nibh euismod tincidunt ut laoreet dolore magna aliquam erat volutpat.</div>
  <div class="abs tiny" style="left:190px;top:104px;width:56px;color:#333">Lorem ipsum dolor sit amet, elit, sed diam nonummy nibh euismod tincidunt ut laoreet dolore magna aliquam erat volutpat.</div>
  <div class="brand">Marula Ridge</div><div class="num">11</div><div class="url">www.marularidge.com</div>
</section>

<section class="slide">
  <div class="title">EDITABLE <b style="color:var(--ink)">CHART</b></div>
  <div class="abs" style="left:66px;top:28px;font-size:8.5px;color:var(--wine)">Diagram title</div>
  <svg class="abs" style="left:0;top:0" width="290" height="162" font-family="Montserrat,sans-serif">
    <g font-size="3.5" fill="#666" text-anchor="end"><text x="20" y="57">80</text><text x="20" y="67">70</text><text x="20" y="77">60</text><text x="20" y="87">50</text><text x="20" y="97">40</text><text x="20" y="107">30</text><text x="20" y="117">20</text><text x="20" y="127">10</text><text x="20" y="137">0</text></g>
    <path d="M22 136 H170" stroke="#333" stroke-width=".5"/>
    <g fill="#98392d"><rect x="30" y="91" width="5" height="45"/><rect x="56" y="71" width="5" height="65"/><rect x="82" y="101" width="5" height="35"/><rect x="108" y="66" width="5" height="70"/><rect x="134" y="71" width="5" height="65"/><rect x="160" y="81" width="5" height="55"/></g>
    <g fill="#8a8a8a"><rect x="35" y="76" width="5" height="60"/><rect x="61" y="91" width="5" height="45"/><rect x="87" y="71" width="5" height="65"/><rect x="113" y="61" width="5" height="75"/><rect x="139" y="111" width="5" height="25"/><rect x="165" y="88" width="5" height="48"/></g>
    <g font-size="3.5" fill="#666" text-anchor="middle"><text x="35" y="142">A</text><text x="61" y="142">B</text><text x="87" y="142">C</text><text x="113" y="142">D</text><text x="139" y="142">E</text><text x="165" y="142">F</text></g>
  </svg>
  <div class="abs" style="left:176px;top:52px;font-size:6.5px;color:var(--wine)">INFORMATION</div>
  <div class="abs tiny" style="left:176px;top:66px;width:88px">Lorem ipsum dolor sit amet, elit, sed diam nonummy nibh euismod tincidunt ut laoreet dolore magna aliquam erat volutpat.<br><br>Lorem ipsum dolor sit amet, elit, sed diam nonummy nibh euismod tincidunt ut laoreet dolore magna aliquam erat volutpat.</div>
  <div class="foot"></div><div class="brand">Marula Ridge</div><div class="num">12</div><div class="url">www.marularidge.com</div>
</section>

<section class="slide">
  <div class="photo ph-build" style="left:0;top:0;width:194px;height:162px" role="img" aria-label="Photo of a three storey residential building against a blue sky"></div>
  <div class="abs" style="left:0;top:0;width:98px;height:162px;background:var(--wine-soft)"></div>
  <div class="abs tiny w" style="left:12px;top:46px;width:80px">Marula Ridge Properties has over 16 years' experience in building construction in South Africa.<br><br>Over the years we have successfully completed building construction projects for public and private sector clients.<br><br>Our expertise are Project Management, Architectural Design, Building Consulting and Sub-contractor Management.</div>
  <div class="abs" style="left:194px;top:0;right:0;bottom:0;background:#fff"></div>
  <div class="abs" style="left:194px;top:11px;font-size:8.5px;line-height:1.25">BUILDING<br><span style="color:var(--wine)">CONSTRUCTION</span></div>
  <svg class="abs" style="left:194px;top:48px" width="16" height="100"><g fill="#98392d"><rect x="1" y="4" width="12" height="12"/><rect x="1" y="36" width="12" height="12"/><rect x="1" y="70" width="12" height="12"/></g><g fill="#fff"><rect x="4" y="8" width="6" height="6"/><rect x="4" y="39" width="6" height="7"/><path d="M3 80 v-4 l4 -3 l4 3 v4z"/></g></svg>
  <div class="abs label" style="left:214px;top:51px">RESIDENTIAL<br>BUILDINGS</div>
  <div class="abs label" style="left:214px;top:82px">COMMERCIAL<br>AND INDUSTRIAL<br>BUILDINGS</div>
  <div class="abs label" style="left:214px;top:116px">SERVICE AND<br>PUBLIC<br>BUILDINGS</div>
  <div class="foot"></div><div class="brand" style="color:#fff">Marula Ridge</div><div class="num">13</div><div class="url">www.marularidge.com</div>
</section>

<section class="slide">
  <div class="photo ph-road" style="left:0;top:0;right:0;height:106px" role="img" aria-label="Photo of a newly tarred curving road through grassland"></div>
  <div class="abs" style="left:0;top:0;width:102px;height:106px;background:var(--wine-soft)"></div>
  <div class="abs tiny w" style="left:12px;top:16px;width:84px">Marula Ridge Properties has extensive experience in the provision of turnkey solutions for varied civil construction projects.<br><br>Using our own plant equipment, we continue to deliver on Roads and Earthworks, Water and Sanitation, as well as the building and maintenance of Civil Structures in South Africa.</div>
  <div class="abs" style="left:12px;top:116px;font-size:8.5px;line-height:1.25">ROAD AND CIVIL<br><span style="color:var(--wine)">CONTRUCTION</span></div>
  <svg class="abs" style="left:0;top:96px" width="290" height="20"><g fill="#98392d"><rect x="118" y="2" width="14" height="14"/><rect x="180" y="2" width="14" height="14"/><rect x="242" y="2" width="14" height="14"/></g><g fill="#fff"><rect x="121" y="8" width="8" height="5"/><path d="M187 5 q4 5 0 9 q-4 -4 0 -9z"/><path d="M245 14 v-5 l4 -4 l4 4 v5z"/></g></svg>
  <div class="abs label" style="left:110px;top:120px">ROADS<br>AND<br>EARTHWORKS</div>
  <div class="abs label" style="left:172px;top:120px">WATER<br>AND<br>SANITATION</div>
  <div class="abs label" style="left:234px;top:120px">CIVIL<br>STRUCTURES</div>
  <div class="foot"></div><div class="brand">Marula Ridge</div><div class="num">14</div><div class="url">www.marularidge.com</div>
</section>

<section class="slide">
  <div class="photo ph-build" style="inset:0" role="img" aria-label="Photo of modern white and grey townhouses"></div>
  <div class="abs" style="left:0;top:0;width:124px;height:162px;background:var(--wine-soft)"></div>
  <div class="abs" style="left:24px;top:13px;font-size:8.5px;line-height:1.25;color:#fff">PROPERTY<br>DEVELOPMENT</div>
  <div class="abs tiny w" style="left:24px;top:48px;width:94px">Marula Ridge Properties works in tandem with Kestrel Holdings, a Marula Ridge company, in the development of real estate infrastructure throughout South Africa.<br><br>We are a multi-faceted and well established property development company acting as both owner and contractor in the specialised building and development of Gated Residential Estates, Rental Apartment Blocks, Domestic Complexes and Business Campuses in South Africa.</div>
  <div class="foot"></div><div class="brand" style="color:#fff">Marula Ridge</div><div class="num">15</div><div class="url">www.marularidge.com</div>
</section>

<section class="slide">
  <div class="title sm">BUILDING CONSTRUCTION <b>GALLERY</b></div>
  <div class="redbox" style="left:12px;top:28px;width:52px;height:66px;justify-content:flex-start;padding-left:5px;text-align:left;line-height:2.6">RESIDENTIAL<br>BUILDINGS</div>
  <div class="photo ph-build" style="left:66px;top:28px;width:118px;height:66px" role="img" aria-label="Photo of a residential estate with low rise blocks"></div>
  <div class="photo" style="left:186px;top:28px;width:92px;height:66px;background:linear-gradient(90deg,#d8d2c4,#3a78c4 40%,#d9d0c0)" role="img" aria-label="Photo of an apartment block with a blue stairwell"></div>
  <div class="photo ph-sky" style="left:12px;top:96px;width:86px;height:52px" role="img" aria-label="Photo of rows of new houses"></div>
  <div class="photo ph-earth" style="left:100px;top:96px;width:92px;height:52px" role="img" aria-label="Photo of red roofed houses on open land"></div>
  <div class="photo ph-build" style="left:194px;top:96px;width:84px;height:52px" role="img" aria-label="Photo of a three storey residential block"></div>
  <div class="foot"></div><div class="brand">Marula Ridge</div><div class="num">16</div><div class="url">www.marularidge.com</div>
</section>

<section class="slide">
  <div class="title sm">BUILDING CONSTRUCTION <b>GALLERY</b></div>
  <div class="redbox" style="left:36px;top:32px;width:150px;height:16px">COMMERCIAL AND INDUSTRIAL BUILDINGS</div>
  <div class="photo ph-build" style="left:36px;top:56px;width:150px;height:92px" role="img" aria-label="Photo of a large industrial building with many windows"></div>
  <div class="photo ph-sky" style="left:190px;top:28px;width:64px;height:38px" role="img" aria-label="Photo of a commercial building corner"></div>
  <div class="photo ph-gray" style="left:190px;top:70px;width:64px;height:38px" role="img" aria-label="Photo of a white office block"></div>
  <div class="photo ph-build" style="left:190px;top:112px;width:64px;height:36px" role="img" aria-label="Photo of a commercial building exterior"></div>
  <div class="foot"></div><div class="brand">Marula Ridge</div><div class="num">17</div><div class="url">www.marularidge.com</div>
</section>

<section class="slide">
  <div class="title sm">BUILDING CONSTRUCTION <b>GALLERY</b></div>
  <div class="photo ph-dark" style="left:16px;top:34px;width:86px;height:54px" role="img" aria-label="Photo of a modern red and glass public building"></div>
  <div class="redbox" style="left:104px;top:34px;width:86px;height:54px">SERVICE AND<br>PUBLIC<br>BUILDINGS</div>
  <div class="photo ph-sky" style="left:192px;top:34px;width:82px;height:54px" role="img" aria-label="Photo of a glass office tower"></div>
  <div class="photo ph-dark" style="left:16px;top:90px;width:86px;height:50px" role="img" aria-label="Photo of a boardroom interior"></div>
  <div class="photo ph-dark" style="left:104px;top:90px;width:86px;height:50px" role="img" aria-label="Photo of an office lobby interior"></div>
  <div class="photo ph-dark" style="left:192px;top:90px;width:82px;height:50px" role="img" aria-label="Photo of a conference room interior"></div>
  <div class="foot"></div><div class="brand">Marula Ridge</div><div class="num">18</div><div class="url">www.marularidge.com</div>
</section>

<section class="slide">
  <div class="title sm">ROAD AND CIVIL CONTRUCTION <b>GALLERY</b></div>
  <div class="photo ph-road" style="left:40px;top:26px;width:104px;height:58px" role="img" aria-label="Photo of road earthworks with machinery"></div>
  <div class="photo ph-road" style="left:146px;top:26px;width:104px;height:58px" role="img" aria-label="Photo of a straight tarred road with kerbs"></div>
  <div class="photo ph-road" style="left:40px;top:86px;width:104px;height:58px" role="img" aria-label="Photo of a curving road through hills"></div>
  <div class="photo ph-road" style="left:146px;top:86px;width:104px;height:58px" role="img" aria-label="Photo of a truck on a road construction site"></div>
  <div class="redbox" style="left:104px;top:58px;width:82px;height:52px">ROADS AND<br>EARTH WORKS</div>
  <div class="foot"></div><div class="brand">Marula Ridge</div><div class="num">19</div><div class="url">www.marularidge.com</div>
</section>

<section class="slide">
  <div class="title sm">ROAD AND CIVIL CONTRUCTION <b>GALLERY</b></div>
  <div class="photo ph-earth" style="left:40px;top:26px;width:104px;height:58px" role="img" aria-label="Photo of a trench dug in red soil"></div>
  <div class="photo ph-earth" style="left:146px;top:26px;width:104px;height:58px" role="img" aria-label="Photo of workers and an excavator on site"></div>
  <div class="photo ph-earth" style="left:40px;top:86px;width:104px;height:58px" role="img" aria-label="Photo of a pipeline trench in a field"></div>
  <div class="photo" style="left:146px;top:86px;width:104px;height:58px;background:linear-gradient(160deg,#a0704c,#b37a50 40%,#4b93d6 70%,#8a5a3a)" role="img" aria-label="Photo of large blue water pipes on red soil"></div>
  <div class="redbox" style="left:104px;top:58px;width:82px;height:52px">WATER AND<br>SANITATION</div>
  <div class="foot"></div><div class="brand">Marula Ridge</div><div class="num">20</div><div class="url">www.marularidge.com</div>
</section>

<section class="slide">
  <div class="title sm">ROAD AND CIVIL CONTRUCTION <b>GALLERY</b></div>
  <div class="photo ph-earth" style="left:40px;top:26px;width:104px;height:58px" role="img" aria-label="Photo of a concrete structure foundation"></div>
  <div class="photo ph-sky" style="left:146px;top:26px;width:104px;height:58px" role="img" aria-label="Photo of a concrete reservoir under construction"></div>
  <div class="photo ph-road" style="left:40px;top:86px;width:104px;height:58px" role="img" aria-label="Photo of a steel frame structure"></div>
  <div class="photo ph-earth" style="left:146px;top:86px;width:104px;height:58px" role="img" aria-label="Photo of reinforced concrete works"></div>
  <div class="redbox" style="left:104px;top:58px;width:82px;height:52px">CIVIL<br>STRUCTURES</div>
  <div class="foot"></div><div class="brand">Marula Ridge</div><div class="num">21</div><div class="url">www.marularidge.com</div>
</section>

<section class="slide">
  <div class="title sm">PROPERTY DEVELOPMENT <b>GALLERY</b></div>
  <div class="photo ph-build" style="left:16px;top:24px;width:100px;height:58px" role="img" aria-label="Photo of a street of modern townhouses"></div>
  <div class="redbox" style="left:122px;top:24px;width:74px;height:26px">THE ALOE<br>LUXURY<br>RESIDENTIAL</div>
  <div class="photo ph-gray" style="left:122px;top:52px;width:74px;height:42px" role="img" aria-label="Photo of a stone clad house entrance"></div>
  <div class="photo ph-build" style="left:202px;top:24px;width:74px;height:126px" role="img" aria-label="Photo of a tall modern residential building"></div>
  <div class="photo ph-gray" style="left:16px;top:86px;width:100px;height:64px" role="img" aria-label="Photo of townhouses along a paved lane"></div>
  <div class="photo ph-sky" style="left:122px;top:98px;width:74px;height:52px" role="img" aria-label="Photo of a modern white villa"></div>
  <div class="foot"></div><div class="brand">Marula Ridge</div><div class="num">22</div><div class="url">www.marularidge.com</div>
</section>

<section class="slide">
  <div class="title sm">FEATURED CONSTRUCTION <b>PROJECTS</b></div>
  <div class="photo ph-road" style="left:12px;top:30px;width:86px;height:50px" role="img" aria-label="Aerial photo of a residential estate"></div>
  <div class="photo ph-build" style="left:102px;top:30px;width:86px;height:50px" role="img" aria-label="Photo of modern townhouses"></div>
  <div class="photo ph-earth" style="left:192px;top:30px;width:86px;height:50px" role="img" aria-label="Photo of a row of new houses"></div>
  <div class="photo ph-road" style="left:12px;top:88px;width:86px;height:50px" role="img" aria-label="Photo of a water treatment plant"></div>
  <div class="photo ph-dark" style="left:102px;top:88px;width:86px;height:50px" role="img" aria-label="Photo of a modern college building"></div>
  <div class="photo ph-sky" style="left:192px;top:88px;width:86px;height:50px" role="img" aria-label="Photo of a residential apartment block"></div>
  <div class="redbox cap" style="left:12px;top:70px;width:86px;height:10px">Kingsley Residential</div>
  <div class="redbox cap" style="left:102px;top:70px;width:86px;height:10px">The Aloe Heights</div>
  <div class="redbox cap" style="left:192px;top:70px;width:86px;height:10px">Riverbend</div>
  <div class="redbox cap" style="left:12px;top:128px;width:86px;height:10px">Waste Water Treatment Plant</div>
  <div class="redbox cap" style="left:102px;top:128px;width:86px;height:10px">Summit College</div>
  <div class="redbox cap" style="left:192px;top:128px;width:86px;height:10px">Belle Vista</div>
  <div class="foot"></div><div class="brand">Marula Ridge</div><div class="num">23</div><div class="url">www.marularidge.com</div>
</section>

<section class="slide" style="background:#efefef">
  <div class="abs" style="left:0;right:0;top:22px;text-align:center;font-size:19px;font-weight:300;letter-spacing:.8px;color:#222;padding-left:10px">THANK YOU</div>
  <svg class="abs" style="left:140px;top:64px" width="12" height="80" fill="#98392d">
    <path d="M6 4 c-3 0 -4 2 -4 4 c0 3 4 6 4 6 s4 -3 4 -6 c0 -2 -1 -4 -4 -4z"/>
    <path d="M3 26 l2 -1 l2 3 l-1 1 q1 3 3 4 l1 -1 l3 2 l-1 2 q-5 0 -9 -10z"/>
    <rect x="2" y="44" width="8" height="7" rx="1"/>
    <circle cx="6" cy="68" r="4.5" fill="none" stroke="#98392d" stroke-width="1.4"/>
  </svg>
  <div class="abs" style="left:162px;top:66px;font-size:5px;line-height:1.35;color:#333">HEAD OFFICE<br>42 Oak Avenue, Rosebank West,<br>Johannesburg, 2041</div>
  <div class="abs" style="left:162px;top:90px;font-size:5px;color:#333">+27 11 555 0142</div>
  <div class="abs" style="left:162px;top:109px;font-size:5px;color:#333">+27 11 555 0187</div>
  <div class="abs" style="left:162px;top:127px;font-size:5px;color:#333">info@marularidge.com</div>
</section>

</main>
</body>
</html>
```